Tarrow Water Taxi and Transport Flyer

I need a business flyer for my new water taxi and freight transport business I have started here in Kodiak Alaska. Kodiak is a remote island in the middle of the gulf of Alaska. There are seven native villages around the island and Kodiak is the #2 fishing port in the United States. We also have the largest Coast Guard Base in the U.S.
My company will be providing water taxi and freight transport logistics to the villages and many hunting and fishing lodges as well as remote properties around the island.

I would like a business flyer that isn't status quo, something that stands out. I do like clean minimal designs but it needs to have the necessary contact info on it.

Target Market(s)

remote lodge / property owners, residents of the many villages around the island and anyone wanting to enjoy the great outdoors of Kodiak Alaska

Industry/Entity Type

Business

Colors
0355a3
0493ce
3277b5
9bcb3c
abd037
faa54b
f78f20
f37122
f68d4d

Requirements
Must have
• logo and necessary contact info
• Captain Morgan Haskell
• www.tarrowferrylink.com
• morgan@tarrowferrylink.com

```html
<!DOCTYPE html>
<html lang="en">
<head>
<meta charset="utf-8">
<title>Tarrow Water Taxi and Transport Flyer</title>
<link rel="stylesheet" href="https://fonts.googleapis.com/css2?family=Oswald:wght@500;600&family=Quicksand:wght@500;600&family=Roboto:wght@300;400&display=swap">
<style>
  :root {
    --page-bg: #e6e8ea;
    --paper: #ffffff;
    --ink: #1d1d1f;
    --ink-soft: #4a4d52;
    --navy: #0d2e4f;
    --deep-blue: #0355a3;
    --bright-blue: #0493ce;
    --mid-blue: #3277b5;
    --sky: #9fc8ea;
    --wood-dark: #7a3414;
    --wood: #b45a2a;
    --steel: #c9ccd0;
  }
  * { box-sizing: border-box; margin: 0; padding: 0; }
  html, body {
    width: 1200px; height: 1000px; overflow: hidden;
    background: var(--page-bg);
  }
  .flyer {
    position: absolute; left: 160px; top: 60px;
    width: 880px; height: 880px;
    background: var(--paper);
    overflow: hidden;
    box-shadow: 0 8px 30px rgba(0,0,0,.18);
  }
  .photo {
    position: absolute; left: 0; bottom: 0; width: 880px; height: 430px;
    background:
      linear-gradient(90deg, rgba(255,255,255,.95) 0%, rgba(255,255,255,0) 45%),
      linear-gradient(180deg, var(--sky) 30%, #d8e7f3 50%, var(--mid-blue) 62%, var(--deep-blue) 80%, var(--navy) 100%);
    -webkit-mask-image: linear-gradient(180deg, transparent 0%, #000 25%);
    mask-image: linear-gradient(180deg, transparent 0%, #000 25%);
  }
  .photo-left {
    position: absolute; left: 0; bottom: 0; width: 520px; height: 220px;
    background: linear-gradient(180deg, rgba(50,119,181,0) 0%, var(--mid-blue) 40%, var(--deep-blue) 100%);
    -webkit-mask-image: linear-gradient(90deg, #000 60%, transparent 100%);
    mask-image: linear-gradient(90deg, #000 60%, transparent 100%);
  }
  .services-art {
    position: absolute; left: 0; top: 0; width: 300px; height: 160px;
    background: linear-gradient(160deg, var(--steel) 0%, #e9eaec 35%, var(--wood) 55%, var(--wood-dark) 100%);
    border-radius: 0 0 80px 0;
    opacity: .9;
  }
  .services-label {
    position: absolute; left: 62px; top: 70px;
    transform: rotate(-24deg);
    font-family: "Oswald", sans-serif; font-weight: 600;
    font-size: 28px; letter-spacing: 2px;
    color: #4a1a06;
  }
  .services-list {
    position: absolute; left: 30px; top: 205px; width: 390px;
    font-family: "Quicksand", sans-serif; font-weight: 500;
    font-size: 16px; line-height: 1.32; text-align: center;
    color: var(--ink);
    white-space: nowrap;
  }
  .headline {
    position: absolute; right: 40px; top: 130px; width: 400px;
    font-family: "Oswald", sans-serif; font-weight: 600;
    text-transform: uppercase; text-align: center; line-height: .95;
    white-space: nowrap;
    background: linear-gradient(180deg, var(--navy) 0%, var(--mid-blue) 55%, var(--bright-blue) 100%);
    -webkit-background-clip: text; background-clip: text; color: transparent;
  }
  .headline .line-top { display: block; font-size: 56px; letter-spacing: 3px; }
  .headline .line-place { display: block; font-size: 118px; letter-spacing: 2px; }
  .headline .line-bottom { display: block; font-size: 64px; letter-spacing: 2px; }
  .tagline {
    position: absolute; right: 60px; top: 395px;
    font-family: "Roboto", sans-serif; font-weight: 400;
    font-size: 18px; line-height: 1.3; text-align: right;
    color: var(--ink-soft);
  }
  .brand {
    position: absolute; left: 80px; top: 455px; width: 320px;
    display: flex; flex-direction: column; align-items: center; gap: 8px;
  }
  .brand-dot {
    width: 40px; height: 40px; border-radius: 50%;
    background: var(--bright-blue);
  }
  .brand-name {
    font-family: "Quicksand", sans-serif; font-weight: 600;
    font-size: 15px; color: var(--deep-blue); text-align: center;
    white-space: nowrap;
  }
  .contact {
    position: absolute; left: 60px; top: 540px; width: 360px;
    font-family: "Roboto", sans-serif; font-weight: 300;
    font-size: 19px; line-height: 1.3; text-align: center;
    color: var(--ink-soft);
  }
</style>
</head>
<body>
  <main class="flyer">
    <div class="photo" role="img" aria-label="Photo of aluminium water taxi boats on blue water under a cloudy sky, with a floatplane wing in the foreground"></div>
    <div class="photo-left" role="img" aria-label="Boat wake on open water"></div>

    <div class="services-art" role="img" aria-label="Illustration of a pocket knife with a wooden handle"></div>
    <div class="services-label">OUR SERVICES</div>

    <p class="services-list">
      Pick up or drop off to and from your location,<br>
      Large front deck for cargo or wild life viewing<br>
      spacious back deck for sitting in the sun,<br>
      listening to music and watching the scenery.<br>
      A knowledgeable and friendly captain<br>
      Some of the best customer service you will<br>
      receive anywhere.
    </p>

    <h1 class="headline">
      <span class="line-top">Your trip to</span>
      <span class="line-place">Kodiak</span>
      <span class="line-bottom">Start here</span>
    </h1>

    <p class="tagline">
      We provide water taxi<br>
      &amp; freight transport services<br>
      to the Kodiak area
    </p>

    <div class="brand">
      <span class="brand-dot"></span>
      <span class="brand-name">Tarrow Water Taxi and Transport</span>
    </div>

    <p class="contact">
      Further info:<br>
      Captain Morgan Haskell<br>
      www.tarrowferrylink.com<br>
      morgan@tarrowferrylink.com
    </p>
  </main>
</body>
</html>
```